Webdesign mit Grundfarbe Weinrot für allgemeine Steuerberatung
Zielgruppe
Allgemeine Steuerberatung. Zielgruppe ist breit gefächert, allerdings soll die Webseite eher den Jungunternehmer ansprechen.
Aufgabenstellung
Die Grundfarbe sollte weinrot sein.

```html
<!DOCTYPE html>
<html lang="de">
<head>
<meta charset="utf-8">
<title>Steuerberatung Helene Brandt – Infothek</title>
<link href="https://fonts.googleapis.com/css2?family=Poppins:wght@400;500;600&family=Source+Serif+4:wght@400&display=swap" rel="stylesheet">
<style>
:root{
  --wine:#921716;
  --wine-dim:#6a3a3a;
  --panel:#f0f0f0;
  --ink:#3c3c3c;
  --body:#404040;
  --rule:#c9c9c9;
  --shade:#5e5e5e;
  --shade-light:#6a6a6a;
  --white:#ffffff;
}
*{margin:0;padding:0;box-sizing:border-box}
html,body{width:1200px;height:2511px;overflow:hidden}
body{position:relative;background:var(--shade-light);font-family:"Source Serif 4",Georgia,serif;color:var(--body)}

.hero{position:absolute;left:0;top:0;width:1200px;height:667px;background:var(--wine)}
.brand{position:absolute;left:0;right:0;top:240px;text-align:center;color:var(--white);font-family:"Source Serif 4",Georgia,serif;font-weight:400;line-height:1}
.brand .name{font-size:64px;letter-spacing:1px}
.brand .role{font-size:44px;margin-top:14px}
.scroll-hint{position:absolute;left:588px;top:606px}

.page-behind{position:absolute;left:0;top:667px;width:172px;height:1764px;overflow:hidden;background:var(--shade-light)}
.photo{position:absolute;left:0;top:0;width:172px;height:563px;background:linear-gradient(160deg,#5a5a5a,#4a4a4a 60%,#555)}
.back{position:absolute;left:132px;top:40px}
.behind-text{position:absolute;left:134px;font-family:"Poppins",Arial,sans-serif;font-weight:600;color:var(--wine-dim);white-space:nowrap}
.behind-h{font-size:30px;line-height:37px}
.behind-s{font-size:18px;line-height:25px}
.behind-li{font-size:18px;line-height:33px;color:#4c4c4c;font-weight:400}
.behind-p{font-family:"Source Serif 4",Georgia,serif;font-size:12px;line-height:21px;color:#4c4c4c;font-weight:400}
.map{position:absolute;left:0;top:1463px;width:172px;height:301px;background:#747474}

.infothek{position:absolute;left:172px;top:667px;width:1028px;height:1764px;background:var(--panel);padding:36px 106px 0 48px}
.infothek h1{font-family:"Poppins",Arial,sans-serif;font-weight:600;font-size:29px;color:var(--ink);line-height:1.2;margin-bottom:26px}
.post{padding:20px 0 15px;border-bottom:1px solid var(--rule)}
.post-date{font-size:16px;line-height:22px;color:var(--ink);margin-bottom:8px}
.post-title{font-family:"Poppins",Arial,sans-serif;font-weight:600;font-size:18px;line-height:24px;color:var(--ink);margin-bottom:8px}
.post-title.is-active{color:var(--wine)}
.post-excerpt{font-size:12.6px;line-height:21px;color:var(--body)}
.read-more{display:inline-block;margin-top:4px;background:var(--wine);color:var(--white);font-family:"Poppins",Arial,sans-serif;font-size:11.5px;line-height:21px;padding:0 9px}
.pagination{margin-top:40px;font-family:"Poppins",Arial,sans-serif;font-weight:600;font-size:11.5px;color:var(--ink);word-spacing:2px}
.pagination .current{color:var(--wine)}

.footer{position:absolute;left:0;top:2431px;width:1200px;height:80px;background:var(--wine);color:var(--white);font-family:"Poppins",Arial,sans-serif;font-size:11.5px}
.footer .copy{position:absolute;left:134px;top:33px}
.footer nav{position:absolute;right:134px;top:33px;display:flex;gap:55px}
</style>
</head>
<body>

<header class="hero">
  <div class="brand">
    <div class="name">Helene Brandt</div>
    <div class="role">Steuerberaterin</div>
  </div>
  <svg class="scroll-hint" width="24" height="14" viewBox="0 0 24 14"><path d="M1 1l11 11L23 1" fill="none" stroke="#fff" stroke-width="2"/></svg>
</header>

<aside class="page-behind">
  <div class="photo" role="img" aria-label="Gedimmtes Porträtfoto einer jungen Frau"></div>
  <svg class="back" width="12" height="20" viewBox="0 0 12 20"><path d="M10 1L2 10l8 9" fill="none" stroke="#fff" stroke-width="2"/></svg>
  <div class="behind-text behind-h" style="top:625px">Le<br>un</div>
  <div class="behind-text behind-s" style="top:765px">Leis<br>Gew</div>
  <div class="behind-text behind-li" style="top:855px">› Bu<br>› Lo<br>› Ja<br>› St</div>
  <div class="behind-text behind-h" style="top:1240px">Üb<br>St</div>
  <div class="behind-text behind-p" style="top:1340px">Meine<br>Branc<br>und Bi<br>abgest</div>
  <div class="map" role="img" aria-label="Gedimmter Lageplan der Kanzlei"></div>
</aside>

<main class="infothek">
  <h1>Infothek und Aktuelles</h1>

  <article class="post">
    <div class="post-date">08.10.2018</div>
    <h2 class="post-title is-active">Lohnsteuer: Aktuelles zum Dienstwagen</h2>
    <p class="post-excerpt">Die Privatnutzung von Dienstwagen ist für viele Arbeitnehmer ein attraktiver Lohnbestandteil, obgleich sich dieser Vorteil in aller Regel steuererhöhend auswirkt. In einem neuen Schreiben, das in allen offenen Fällen anzuwenden ist, hat sich das Bundesfinanzministerium...</p>
    <span class="read-more">Weiterlesen</span>
  </article>

  <article class="post">
    <div class="post-date">08.10.2018</div>
    <h2 class="post-title">Abschreibung bei „Arbeitswohnung“ im Miteigentum eines Ehepaars</h2>
    <p class="post-excerpt">Die Kosten eines außerhäuslichen Arbeitszimmers lassen sich in unbeschränkter Höhe absetzen - selbst wenn dort nicht der Tätigkeitsmittelpunkt liegt. In einem Streitfall vor dem Bundesfinanzhof (BFH) hatte ein Ehepaar gemeinsam eine Wohnung gekauft (hälftige Miteigentumsanteile), die...</p>
    <span class="read-more">Weiterlesen</span>
  </article>

  <article class="post">
    <div class="post-date">08.10.2018</div>
    <h2 class="post-title is-active">Kein Lohnzufluss bei Gehaltsumwandlung für vorzeitigen Ruhestand</h2>
    <p class="post-excerpt">Bei der Einrichtung eines Zeitwertkontos kann der Arbeitnehmer darauf Teile seines fälligen Arbeitslohns „ansparen“, um diesen dann in einer späteren Freistellungsphase ausgezahlt zu bekommen. Gutschriften auf einem Wertguthabenkonto zur Finanzierung eines vorzeitigen Ruhestands sind kein gegenwärtig zufließender Arbeitslohn und daher erst in der Auszahlungsphase zu versteuern. Der Bundesfinanzhof hat gegen die Auffassung der Finanzverwaltung entschieden, dass dies auch für Fremdgeschäftsführer einer GmbH gilt.</p>
  </article>

  <article class="post">
    <div class="post-date">08.10.2018</div>
    <h2 class="post-title">Vermietung eines Homeoffice vom Arbeitnehmer an den Arbeitgeber</h2>
    <p class="post-excerpt">Wenn ein Arbeitnehmer einen Raum seiner Wohnung bzw. seines Hauses an seinen Arbeitgeber vermietet und diesen Raum selbst als Homeoffice nutzt, sind die Mietzahlungen des Arbeitgebers beim Arbeitnehmer als Einkünfte aus Vermietung und Verpachtung zu erfassen. Voraussetzung...</p>
    <span class="read-more">Weiterlesen</span>
  </article>

  <article class="post">
    <div class="post-date">08.10.2018</div>
    <h2 class="post-title">Gewerbeertrag: Hinzurechnungen von Mietzinsen und Lizenzgebühren</h2>
    <p class="post-excerpt">Bei der Berechnung der Gewerbesteuer muss der Gewinn aus Gewerbebetrieb um bestimmte Hinzurechnungen erhöht werden, um zuvor abgesetzte Beträge gewerbesteuerrechtlich teilweise wieder zu neutralisieren. Hinzurechnungen sind zum Beispiel für einen Teil der gezahlten Miet- und...</p>
    <span class="read-more">Weiterlesen</span>
  </article>

  <article class="post">
    <div class="post-date">08.10.2018</div>
    <h2 class="post-title">Briefkastenanschrift reicht für den Vorsteuerabzug aus</h2>
    <p class="post-excerpt">Unternehmer sind zum Vorsteuerabzug berechtigt, wenn ihnen eine ordnungsgemäße Eingangsrechnung vorliegt. Die Rechnung muss unter anderem die vollständige Anschrift des leistenden Unternehmers enthalten. In zwei aktuellen Urteilen hat der Bundesfinanzhof die Anforderunge...</p>
    <span class="read-more">Weiterlesen</span>
  </article>

  <article class="post">
    <div class="post-date">08.10.2018</div>
    <h2 class="post-title">1-%-Regelung: Nutzungsentnahme ist nicht auf 50 % zu deckeln</h2>
    <p class="post-excerpt">Wenn ein privat mitgenutzter Firmenwagen zu mehr als 50 % betrieblich genutzt wird, muss die private Nutzungsentnahme grundsätzlich nach der 1-%-Regelung ermittelt werden. Für jeden Kalendermonat ist 1 % des inländischen Bruttolistenneupreises des Fahrzeugs anzusetzen...</p>
    <span class="read-more">Weiterlesen</span>
  </article>

  <article class="post">
    <div class="post-date">08.10.2018</div>
    <h2 class="post-title">Investitionsabzugsbetrag: Abschreibung im Sonderbetriebsvermögen</h2>
    <p class="post-excerpt">Um Abschreibungspotential von Wirtschaftsgütern des Anlagevermögens schon vor deren Anschaffung nutzen zu können, dürfen kleine und mittlere Betriebe Investitionsabzugsbeträge in Höhe von maximal 40 % der voraussichtlichen Anschaffungskosten bilden. Dadurch können...</p>
    <span class="read-more">Weiterlesen</span>
  </article>

  <article class="post">
    <div class="post-date">08.10.2018</div>
    <h2 class="post-title">Bruttolistenpreis bei Importfahrzeug</h2>
    <p class="post-excerpt">Ist die private Nutzung eines Firmenwagens nach der 1-%-Regelung zu bewerten, ist der inländische Bruttolistenpreis laut Bundesfinanzhof gegebenenfalls zu schätzen, und zwar wenn das Fahrzeug ein Importfahrzeug ist und weder ein inländischer Bruttolistenpreis vorhanden ist...</p>
    <span class="read-more">Weiterlesen</span>
  </article>

  <div class="pagination"><span class="current">1</span> 2 3 4 ... 18</div>
</main>

<footer class="footer">
  <div class="copy">© 2019 - Steuerberatung Helene Brandt</div>
  <nav><span>Datenschutz</span><span>Impressum</span><span>Kontakt</span></nav>
</footer>

</body>
</html>
```